ORB of Quietharbour Business Card Rebrand

Hello Designers! We are looking for help designing our new business card to go in conjunction with our company rebrand. Unfortunately, we have an event mid June that requires we get these printed ASAP (before our new website is launched.) We have a mostly complete Brand Book which I have uploaded to this request for your reference to company information, style, fonts. I've also enclosed our logo file in .eps & .jpg. Attached is a sample business card my boss liked but said was "too simple." I made it in Canva and do not profess to be a designer. NOT FOR DESIGN REFERENCE, ONLY FOR CONTEXT Here is what our old website looks like: https://orbofquietharbour.example/.
Sick
Gathering more feedback
Sick
Sick

```html
<!DOCTYPE html>
<html lang="en">
<head>
<meta charset="utf-8">
<title>ORB of Quietharbour – Business Card</title>
<link href="https://fonts.googleapis.com/css2?family=Montserrat:wght@400;500;700&display=swap" rel="stylesheet">
<style>
  :root {
    --stage: #2a2a2a;
    --card-white: #ffffff;
    --card-black: #0f0f0f;
    --pattern-light: #4a4a4a;
    --pattern-mid: #262626;
    --ink: #111111;
    --accent: #45b3e7;
    --rule: #9a9a9a;
  }
  * { margin: 0; padding: 0; box-sizing: border-box; }
  html, body { width: 1200px; height: 689px; overflow: hidden; }
  body {
    background: var(--stage);
    font-family: "Montserrat", sans-serif;
    position: relative;
  }
  .card {
    position: absolute;
    top: 195px;
    width: 525px;
    height: 300px;
    border-radius: 26px;
    overflow: hidden;
  }
  .card-back {
    left: 50px;
    background: var(--card-black);
  }
  .back-pattern {
    position: absolute;
    inset: 0;
    background: linear-gradient(215deg, var(--pattern-light) 0%, var(--pattern-mid) 45%, var(--card-black) 80%);
  }
  .back-mark {
    position: absolute;
    left: 372px;
    top: 96px;
    width: 38px;
    height: 38px;
    border-radius: 50%;
    background: var(--accent);
  }
  .card-front {
    left: 625px;
    background: var(--card-white);
  }
  .brand {
    position: absolute;
    left: 34px;
    top: 118px;
    display: flex;
    align-items: center;
    gap: 10px;
  }
  .brand-dot {
    width: 58px; height: 58px;
    border-radius: 50%;
    background: var(--accent);
    flex: none;
  }
  .brand-name {
    font-weight: 700;
    font-size: 15px;
    line-height: 1.15;
    color: var(--ink);
    width: 120px;
  }
  .divider {
    position: absolute;
    left: 218px;
    top: 88px;
    width: 1px;
    height: 126px;
    background: var(--rule);
  }
  .details {
    position: absolute;
    left: 240px;
    top: 86px;
  }
  .person-name {
    font-weight: 700;
    font-size: 20px;
    letter-spacing: 0.2px;
    color: var(--ink);
    text-transform: uppercase;
  }
  .person-role {
    font-weight: 500;
    font-size: 16px;
    color: var(--accent);
    margin-top: 1px;
  }
  .contacts { list-style: none; margin-top: 14px; }
  .contacts li {
    display: flex;
    align-items: center;
    gap: 9px;
    font-size: 13.5px;
    font-weight: 500;
    color: var(--ink);
    margin-bottom: 7px;
    white-space: nowrap;
  }
  .icon {
    width: 20px; height: 20px;
    border-radius: 50%;
    background: var(--accent);
    display: flex; align-items: center; justify-content: center;
    flex: none;
  }
  .icon svg { width: 12px; height: 12px; fill: #fff; }
</style>
</head>
<body>
  <div class="card card-back">
    <div class="back-pattern" role="img" aria-label="Repeating pattern of the brand mark in grey tones over black"></div>
    <span class="back-mark"></span>
  </div>

  <div class="card card-front">
    <div class="brand">
      <span class="brand-dot"></span>
      <span class="brand-name">ORB of Quietharbour</span>
    </div>
    <div class="divider"></div>
    <div class="details">
      <p class="person-name">Miles Hartwell-Osk</p>
      <p class="person-role">Managing Partner</p>
      <ul class="contacts">
        <li>
          <span class="icon"><svg viewBox="0 0 24 24"><path d="M6.6 10.8a15 15 0 0 0 6.6 6.6l2.2-2.2a1 1 0 0 1 1-.25 11.4 11.4 0 0 0 3.6.57 1 1 0 0 1 1 1V20a1 1 0 0 1-1 1A17 17 0 0 1 3 4a1 1 0 0 1 1-1h3.5a1 1 0 0 1 1 1c0 1.25.2 2.45.57 3.57a1 1 0 0 1-.25 1z"/></svg></span>
          +945-555-0142
        </li>
        <li>
          <span class="icon"><svg viewBox="0 0 24 24"><path d="M3 5h18v14H3z"/><path d="M4 6.5l8 6.2 8-6.2" stroke="#45b3e7" stroke-width="1.6" fill="none"/></svg></span>
          miles@orbofquietharbour.example
        </li>
        <li>
          <span class="icon"><svg viewBox="0 0 24 24"><path d="M12 2a7 7 0 0 0-7 7c0 5.2 7 13 7 13s7-7.8 7-13a7 7 0 0 0-7-7zm0 9.5A2.5 2.5 0 1 1 12 6.5a2.5 2.5 0 0 1 0 5z"/></svg></span>
          Riverton, GA based (Central Time)
        </li>
      </ul>
    </div>
  </div>
</body>
</html>
```